Orvane Slab Hub

- Brochure design

Target Market(s)

Granite and Quartz

Font styles to use
Sans Serif

Colors

Designer to choose colors to be used in the design.

Requirements
Must have
• I post the instruction file below
Nice to have
Should not have

```html
<!DOCTYPE html>
<html lang="en">
<head>
<meta charset="utf-8">
<title>Orvane Slab Hub – Product Catalog Brochure</title>
<link href="https://fonts.googleapis.com/css2?family=Roboto:wght@400;500;900&family=Roboto+Condensed:wght@300;400;700&display=swap" rel="stylesheet">
<style>
  :root {
    --bg: #d9dadc;
    --paper: #ffffff;
    --panel-grey: #e6e7e9;
    --ink: #111111;
    --ink-soft: #2a2a2a;
    --band: #0c0c0c;
    --band-text: #f2f2f2;
    --tag-band: #d4d5d7;
  }
  * { box-sizing: border-box; margin: 0; padding: 0; }
  html, body { width: 1200px; height: 1200px; overflow: hidden; }
  body {
    background: var(--bg);
    font-family: "Roboto", Arial, sans-serif;
    color: var(--ink);
    position: relative;
  }
  .spread {
    position: absolute;
    left: 40px; top: 255px;
    width: 1120px; height: 690px;
    display: flex;
    background: var(--paper);
    box-shadow: 0 10px 30px rgba(0,0,0,0.15);
  }
  .panel { position: relative; width: 560px; height: 690px; overflow: hidden; }

  /* Back panel */
  .about-header {
    height: 62px; background: var(--paper);
    padding: 16px 0 0 38px;
  }
  .about-title {
    font-weight: 900; font-size: 30px; letter-spacing: 1px;
  }
  .about-body {
    height: 338px; background: var(--panel-grey);
    padding: 30px 46px 0 40px;
  }
  .about-body p {
    font-size: 13.2px; line-height: 1.42; text-align: justify;
    color: var(--ink-soft); margin-bottom: 14px;
  }
  .swatches { display: flex; height: 80px; }
  .swatch { flex: 1; }
  .footer {
    display: flex; padding: 38px 0 0 40px; height: 210px;
  }
  .footer-contact { width: 285px; }
  .footer-name { font-size: 15px; font-weight: 500; margin-bottom: 18px; }
  .footer-contact p, .footer-hours p { font-size: 11.5px; line-height: 1; margin-bottom: 14px; }
  .footer-divider { width: 1px; background: var(--ink); height: 140px; margin-top: 0; }
  .footer-hours { padding: 46px 0 0 55px; }

  /* Front panel */
  .cover-photo {
    position: absolute; left: 0; top: 0; width: 560px; height: 400px;
    background: linear-gradient(180deg, #eef0f1 0%, #d8dadb 35%, #9c9891 62%, #3a3634 78%, #b08a60 100%);
  }
  .cover-brand {
    position: absolute; left: 22px; top: 18px;
    font-size: 20px; font-weight: 500; color: var(--ink);
  }
  .cover-tags {
    position: absolute; right: 0; top: 0; height: 34px; width: 300px;
    background: var(--tag-band);
    display: flex; justify-content: space-around; align-items: center;
    font-family: "Roboto Condensed", Arial, sans-serif; font-size: 10px; letter-spacing: .5px;
  }
  .cover-swatches { position: absolute; left: 0; top: 400px; width: 560px; }
  .cover-title {
    position: absolute; left: 0; top: 505px; width: 560px; text-align: center;
    font-family: "Roboto Condensed", Arial, sans-serif;
  }
  .cover-title .name { font-weight: 700; font-size: 34px; letter-spacing: .5px; }
  .cover-title .catalog { font-weight: 300; font-size: 32px; margin-top: 2px; }
  .cover-band {
    position: absolute; left: 0; top: 605px; width: 560px; height: 30px;
    background: var(--band); color: var(--band-text);
    display: flex; justify-content: center; align-items: center; gap: 14px;
    font-family: "Roboto Condensed", Arial, sans-serif; font-size: 15px; font-weight: 300;
  }
  .cover-url {
    position: absolute; left: 0; top: 652px; width: 560px; text-align: center;
    font-size: 10.5px; font-weight: 500;
  }
</style>
</head>
<body>
<main class="spread">
  <section class="panel panel-back">
    <header class="about-header"><h1 class="about-title">ABOUT US</h1></header>
    <div class="about-body">
      <p>Orvane Slab Hub is a countertop manufacture firm based in Dallas, Texas. Our designers and installers have been creating beautiful granite and quartz pieces for apartment complexes, builders, and fabricators, with multiple projects published in design and decor magazines. Orvane Slab Hub works on projects across the country and is well-known for delivering sophisticated, custom granite and quartz pieces for clients and budgets of all kinds. Orvane Slab Hub prides themselves in high-impact, comprehensively designed environments that are delivered in a professional and timely manner.</p>
      <p>The team of experienced and talented installers will work to create dynamic designs for your residential or commercial project. Design concepts are tailored for each client, maintaining the Orvane Slab Hub philosophy that your surroundings should reflect your lifestyle.</p>
      <p>Projects are carefully selected so that Orvane Slab Hub can maintain a close relationship with each client. Acceptance of a project will be determined by availability of staff and the scope of work.</p>
    </div>
    <div class="swatches">
      <div class="swatch" role="img" aria-label="White veined marble sample" style="background:linear-gradient(135deg,#f2f2f2,#dcdcdc)"></div>
      <div class="swatch" role="img" aria-label="Black quartz sample" style="background:#1c1a1c"></div>
      <div class="swatch" role="img" aria-label="Gold granite sample" style="background:linear-gradient(135deg,#c8a86a,#9c7c46)"></div>
      <div class="swatch" role="img" aria-label="Blue-grey granite sample" style="background:linear-gradient(135deg,#7c8c98,#55636d)"></div>
      <div class="swatch" role="img" aria-label="Brown granite sample" style="background:linear-gradient(135deg,#9a6a56,#6e4434)"></div>
    </div>
    <footer class="footer">
      <div class="footer-contact">
        <div class="footer-name">Orvane Slab Hub</div>
        <p>Store Address: 4820 Mirel Ave, Dallas, TX 75000</p>
        <p>Phone: 352-555-0142</p>
        <p>Email: hello@orvaneslabhub.com</p>
        <p>Website: www.orvaneslabhub.com</p>
      </div>
      <div class="footer-divider"></div>
      <div class="footer-hours">
        <p>Mon - Fri, 8am - 6pm</p>
        <p>Saturday, 9am - 4pm</p>
        <p>Sunday, by appointment</p>
      </div>
    </footer>
  </section>

  <section class="panel panel-front">
    <div class="cover-photo" role="img" aria-label="Bright kitchen with white cabinets and a dark island topped with a pale stone countertop"></div>
    <div class="cover-tags"><span>NATURALLY</span><span>BEAUTIFUL</span><span>PREMIUM QUALITY</span></div>
    <div class="cover-brand">Orvane Slab Hub</div>
    <div class="swatches cover-swatches">
      <div class="swatch" role="img" aria-label="Dark green granite sample" style="background:linear-gradient(135deg,#45452f,#2a2a20)"></div>
      <div class="swatch" role="img" aria-label="Gold granite sample" style="background:linear-gradient(135deg,#b89560,#8e6c3e)"></div>
      <div class="swatch" role="img" aria-label="Grey stone sample" style="background:linear-gradient(135deg,#c6c6c2,#a4a4a0)"></div>
      <div class="swatch" role="img" aria-label="Amber granite sample" style="background:linear-gradient(135deg,#d29c56,#a8743a)"></div>
      <div class="swatch" role="img" aria-label="White and grey granite sample" style="background:linear-gradient(135deg,#d8d4cc,#a8a49c)"></div>
    </div>
    <div class="cover-title">
      <div class="name">ORVANE SLAB HUB</div>
      <div class="catalog">PRODUCT CATALOG 2018</div>
    </div>
    <div class="cover-band">
      <span>pre fabricate slabs</span><span>•</span><span>natural stone</span><span>•</span><span>granite</span><span>•</span><span>quartz</span>
    </div>
    <div class="cover-url">www.orvaneslabhub.com</div>
  </section>
</main>
</body>
</html>
```